New website for Pilates Studio

I need a new version of my website
http://brightcoreflow.biz/
I want an updated fresh look with an easier to read schedule that looks good on mobile phones as well as laptops.
Clean, simple, fresh and BOLD

Target Market(s)

All ages, genders and races

Coding

Number of Pages Required

Colors
9bcb3c

Requirements
Must have
• Photos that mostly use the real images from our studio. Browse our facebook page, website or ask me for high quality images

```html
<!DOCTYPE html>
<html lang="en">
<head>
<meta charset="utf-8">
<title>Bright Core Flow — Pilates Studio</title>
<link href="https://fonts.googleapis.com/css2?family=Lato:ital,wght@0,400;0,700;0,900;1,700&display=swap" rel="stylesheet">
<style>
:root{
  --green:#8cc63f;
  --green-dark:#6f9f2c;
  --footer:#7fa83a;
  --ink:#333;
  --muted:#666;
  --light:#f2f2f2;
  --band:#e6e6e6;
  --line:#d5d5d5;
  --white:#fff;
}
*{box-sizing:border-box;margin:0;padding:0}
html,body{width:851px;height:1200px;overflow:hidden;background:var(--white)}
body{font-family:'Lato',sans-serif;color:var(--ink);position:relative}
.page{position:relative;width:851px;height:1200px;overflow:hidden;background:var(--white)}

/* header */
.site-header{position:absolute;left:0;top:0;width:851px;height:72px;background:var(--white)}
.brand{position:absolute;left:34px;top:18px;display:flex;align-items:center;gap:9px;font-size:22px;font-weight:700;color:var(--green-dark)}
.brand-dot{width:26px;height:26px;border-radius:50%;background:var(--green)}
.main-nav{position:absolute;right:46px;top:30px;display:flex;gap:30px;font-size:11px;font-weight:700;letter-spacing:.5px}
.main-nav a{color:var(--ink);text-decoration:none}
.main-nav a.active{color:var(--green)}
.book-tab{position:absolute;right:38px;top:66px;width:138px;height:30px;background:var(--green);color:var(--white);font-size:12px;font-weight:700;display:flex;align-items:center;justify-content:center;z-index:3}

/* hero */
.hero{position:absolute;left:0;top:80px;width:851px;height:330px;background:linear-gradient(180deg,#3d4a4e 0%,#556367 45%,#2f3a3d 100%)}
.hero-title{position:absolute;left:0;right:0;top:133px;text-align:center;color:var(--white);font-size:29px;font-style:italic;font-weight:700}
.hero-btn{position:absolute;left:377px;top:190px;width:98px;height:30px;background:var(--green);color:var(--white);font-size:12px;font-weight:700;display:flex;align-items:center;justify-content:center}
.hero-arrow{position:absolute;top:150px;width:22px;height:32px;background:rgba(255,255,255,.85);display:flex;align-items:center;justify-content:center}
.hero-arrow.left{left:0}.hero-arrow.right{right:0}

/* services */
.services{position:absolute;left:130px;top:380px;width:592px;display:flex;gap:12px}
.service{flex:1;background:var(--white);height:200px;text-align:center;padding-top:70px;box-shadow:0 1px 3px rgba(0,0,0,.15)}
.service-icon{position:absolute;top:0;width:58px;height:58px;border-radius:50%;background:var(--green);border:4px solid var(--white);box-shadow:0 0 0 1px var(--line);display:flex;align-items:center;justify-content:center}
.service h3{font-size:13px;font-weight:700;margin-bottom:8px}
.service p{font-size:8.5px;color:var(--muted);line-height:1.35;padding:0 28px}
.read-more{display:inline-block;margin-top:10px;background:var(--green-dark);color:var(--white);font-size:8px;font-weight:700;padding:4px 11px}

/* about */
.about{position:absolute;left:36px;top:610px;width:780px;height:200px}
.about h2{font-size:18px;font-weight:700;display:flex;align-items:center;gap:8px}
.about h2 span{color:var(--green-dark)}
.about h2::after{content:"";width:410px;height:1px;background:var(--line)}
.about-text{position:absolute;left:0;top:44px;width:530px;font-size:9px;line-height:1.45;color:var(--muted)}
.about-text p{margin-bottom:8px}
.about-video{position:absolute;right:0;top:0;width:212px;height:128px;background:linear-gradient(135deg,#b9c3c6,#7d8a8d)}
.play{position:absolute;left:92px;top:50px;width:28px;height:28px;border-radius:50%;background:rgba(255,255,255,.85)}

/* cta band */
.cta{position:absolute;left:0;top:835px;width:851px;height:68px;background:var(--band)}
.cta h4{position:absolute;left:36px;top:14px;font-size:16px;font-weight:700;color:#444}
.cta p{position:absolute;left:36px;top:38px;font-size:11px;color:var(--muted)}
.cta-btn{position:absolute;right:36px;top:16px;width:160px;height:36px;background:var(--green);color:var(--white);font-size:16px;font-weight:700;display:flex;align-items:center;justify-content:center}

/* info columns */
.info{position:absolute;left:36px;top:920px;width:780px;height:200px;display:flex}
.col{flex:1;padding:0 16px;border-right:1px solid var(--line)}
.col:last-child{border-right:0;text-align:center}
.col:first-child{padding-left:0}
.col h5{font-size:13px;font-weight:700;margin-bottom:10px;display:flex;align-items:center;gap:6px}
.col:last-child h5{justify-content:center}
.field{height:18px;border:1px solid var(--line);margin-bottom:6px;font-size:8px;color:#888;padding:3px 6px}
.field.tall{height:40px}
.submit{display:inline-block;background:var(--green-dark);color:var(--white);font-size:8px;font-weight:700;padding:5px 12px}
.col p{font-size:8.5px;color:var(--muted);line-height:1.4}
.badge{margin:10px auto 0;width:90px;height:90px;border-radius:50%;background:var(--green);opacity:.85}
.acc{display:flex;flex-direction:column;align-items:center;gap:6px}
.acc div{width:70px;height:40px;background:#cfd6da}
.acc div.round{width:42px;height:42px;border-radius:50%;background:#1f4f8f}

/* footer */
.site-footer{position:absolute;left:0;top:1130px;width:851px;height:70px;background:var(--footer);color:var(--white);text-align:center}
.foot-nav{padding-top:12px;font-size:9px;font-weight:700;letter-spacing:.4px}
.foot-nav span{margin:0 8px}
.copy{font-size:8.5px;margin-top:6px}
.follow{font-size:8.5px;margin-top:6px;display:flex;justify-content:center;align-items:center;gap:5px}
.follow i{width:10px;height:10px;background:var(--white);display:inline-block}
</style>
</head>
<body>
<div class="page">
  <header class="site-header">
    <div class="brand"><span class="brand-dot"></span>Bright Core Flow</div>
    <nav class="main-nav">
      <a class="active" href="#">HOME</a><a href="#">SCHEDULE</a><a href="#">INSTRUCTORS</a><a href="#">RATES</a><a href="#">CONTACT</a>
    </nav>
  </header>
  <div class="book-tab">BOOK YOUR SEAT</div>

  <section class="hero" role="img" aria-label="Photo of a group class stretching in the studio">
    <div class="hero-arrow left"><svg width="8" height="12"><path d="M7 1L2 6l5 5" stroke="#555" stroke-width="2" fill="none"/></svg></div>
    <div class="hero-arrow right"><svg width="8" height="12"><path d="M1 1l5 5-5 5" stroke="#555" stroke-width="2" fill="none"/></svg></div>
    <h1 class="hero-title">Get Ready For One-On-One Fitness Session</h1>
    <div class="hero-btn">GET STARTED »</div>
  </section>

  <section class="services">
    <div class="service" style="position:relative">
      <div class="service-icon" style="left:67px;top:-30px"><svg width="26" height="30" viewBox="0 0 26 30"><circle cx="13" cy="6" r="5" fill="#fff"/><path d="M3 29V18a10 9 0 0 1 20 0v11z" fill="#fff"/></svg></div>
      <h3>One-On-One Session</h3>
      <p>Lorem ipsum dolor sit amet consect etuer adipiscing elit sed diam nonu mmy nibh euismod tincidunt</p>
      <span class="read-more">Read More</span>
    </div>
    <div class="service" style="position:relative">
      <div class="service-icon" style="left:67px;top:-30px"><svg width="32" height="28" viewBox="0 0 32 28"><circle cx="16" cy="5" r="4" fill="#fff"/><circle cx="6" cy="9" r="3" fill="#fff"/><circle cx="26" cy="9" r="3" fill="#fff"/><path d="M9 27V17a7 7 0 0 1 14 0v10z M1 27v-8a5 5 0 0 1 7-4v12z M31 27v-8a5 5 0 0 0-7-4v12z" fill="#fff"/></svg></div>
      <h3>Group Reformer Classes</h3>
      <p>Lorem ipsum dolor sit amet consect etuer adipiscing elit sed diam nonu mmy nibh euismod tincidunt</p>
      <span class="read-more">Read More</span>
    </div>
    <div class="service" style="position:relative">
      <div class="service-icon" style="left:67px;top:-30px"><svg width="30" height="28" viewBox="0 0 30 28"><circle cx="15" cy="5" r="4" fill="#fff"/><path d="M2 14l13-4 13 4-2 2-8-2v6l7 6H5l7-6v-6l-8 2z" fill="#fff"/></svg></div>
      <h3>Mat Classes</h3>
      <p>Lorem ipsum dolor sit amet consect etuer adipiscing elit sed diam nonu mmy nibh euismod tincidunt</p>
      <span class="read-more">Read More</span>
    </div>
  </section>

  <section class="about">
    <h2>About <span>Bright Core Flow</span></h2>
    <div class="about-text">
      <p>Bright Core Flow Pilates and CoreSpiral Studio, in the heart of Larkfield Village, is a warm, inviting studio where students and teachers alike are supported and encouraged to discover and grow at an individual pace through the field of integrated movement.</p>
      <p>We offer one on one sessions, group reformer classes and mat classes.</p>
      <p>Our mission is to promote long term emotional and physical health through joyful, integrated movement training and to inspire and nurture our clients to learn more deeply about themselves and connect with fellow students and the community.</p>
    </div>
    <div class="about-video" role="img" aria-label="Video still of an instructor working with a client on a reformer"><span class="play"></span></div>
  </section>

  <section class="cta">
    <h4>Lorem ipsum dolor sit amet consectetuer adipiscing elit</h4>
    <p>Lorem ipsum dolor sit amet consectetuer adipiscing</p>
    <div class="cta-btn">BOOK YOUR SEAT</div>
  </section>

  <section class="info">
    <div class="col">
      <h5><svg width="12" height="10"><rect x="0.5" y="0.5" width="11" height="9" fill="none" stroke="#333"/><path d="M1 1l5 4 5-4" stroke="#333" fill="none"/></svg>Get In Touch With Us</h5>
      <div class="field">Name</div>
      <div class="field">Email</div>
      <div class="field">Enquiry Type</div>
      <div class="field tall">Your Message</div>
      <span class="submit">SUBMIT</span>
    </div>
    <div class="col">
      <h5>We're Green Certified!</h5>
      <p>Join our community in creating a sustainable future. We enjoy the benefits of protecting our environment with daily practice: recycling, using efficient lighting, conserving water, and acting responsibly.</p>
      <div class="badge"></div>
    </div>
    <div class="col">
      <h5>Our Accreditation</h5>
      <div class="acc"><div></div><div></div><div class="round"></div></div>
    </div>
  </section>

  <footer class="site-footer">
    <div class="foot-nav"><span>HOME</span>|<span>SCHEDULE</span>|<span>INSTRUCTORS</span>|<span>RATES</span>|<span>CONTACT</span></div>
    <div class="copy">© 2015 Bright Core Flow. All Rights Reserved.</div>
    <div class="follow">Follow us <i></i></div>
  </footer>
</div>
</body>
</html>
```